Business Card and Letterhead Design Project

I am starting my own building design business in Melbourne. The business will use my experience to help people make balanced life choices for building and renovating. My target audience is women -particularly mothers. I aim to be approachable and economical. I would like to see a design that uses greens or blues - natural colours. A lot of my work balances design and construction management so design should be flexible.

I want a double sided business card design and a letterhead design that I can use on all office correspondance

Design should have a clean crisp feel - a bit edgey in a feminine way.

Target Market(s)

Potential clients.

Industry/Entity Type

Construction

Requirements
Must have
• Harbourline Design Studio
Rosalind Tebbutt B.Arch

0498 273 461
rosalind@harbourlinedesignstudio.com.au

14 Quandong Street
Ferndale North VIC 3188
harbourlinedesignstudio.com.au
Nice to have
• Should have a calming feel to make me seem approachable but still professional.
Should not have
• No photos on the card or building plans.

```html
<!DOCTYPE html>
<html lang="en">
<head>
<meta charset="utf-8">
<title>Harbourline Design Studio – Stationery</title>
<link rel="stylesheet" href="https://fonts.googleapis.com/css2?family=Marcellus&family=Montserrat:wght@400;500&display=swap">
<style>
  :root {
    --teal: #16809c;
    --grey: #8c8c8c;
    --grey-dark: #6f6f6f;
    --paper: #ffffff;
    --backdrop: #eeeeee;
    --ink: #5a5a5a;
    --serif: "Marcellus", "Times New Roman", serif;
    --sans: "Montserrat", Arial, sans-serif;
  }
  * { box-sizing: border-box; margin: 0; padding: 0; }
  html, body {
    width: 1200px; height: 979px; overflow: hidden;
    background: var(--backdrop);
  }
  .stationery { position: relative; width: 1200px; height: 979px; }

  /* Wordmark */
  .wordmark { font-family: var(--serif); color: var(--teal); text-align: right; line-height: 1.05; }
  .wordmark .name { display: block; letter-spacing: 0.06em; text-transform: uppercase; }
  .wordmark .sub { display: block; letter-spacing: 0.08em; }

  .contact { font-family: var(--sans); font-style: normal; color: var(--ink); line-height: 1.5; }
  .contact b { color: var(--teal); font-weight: 500; }

  /* Letterhead */
  .letterhead {
    position: absolute; left: 90px; top: 110px;
    width: 540px; height: 764px;
    background: var(--paper);
    box-shadow: 0 2px 10px rgba(0,0,0,0.08);
  }
  .letterhead .wordmark { position: absolute; right: 44px; top: 44px; }
  .letterhead .wordmark .name { font-size: 30px; }
  .letterhead .wordmark .sub { font-size: 17px; }
  .letterhead .contact { position: absolute; left: 44px; top: 150px; font-size: 9px; }
  .footer-band { position: absolute; left: 0; right: 0; bottom: 0; height: 20px; }
  .footer-band .grey { position: absolute; left: 0; bottom: 0; width: 100%; height: 12px; background: var(--grey); }
  .footer-band .teal { position: absolute; right: 0; bottom: 12px; width: 33%; height: 8px; background: var(--teal); }
  .footer-band .teal-edge { position: absolute; right: 0; bottom: 0; width: 33%; height: 12px; background: var(--grey-dark); }

  /* Cards */
  .card {
    position: absolute; width: 420px; height: 240px;
    box-shadow: 0 2px 10px rgba(0,0,0,0.08);
    overflow: hidden;
  }
  .card-front { left: 700px; top: 560px; background: var(--paper); }
  .card-front .wordmark { position: absolute; right: 30px; top: 28px; }
  .card-front .wordmark .name { font-size: 24px; }
  .card-front .wordmark .sub { font-size: 14px; }
  .card-front .holder {
    position: absolute; left: 30px; top: 128px;
    font-family: var(--sans); font-weight: 500; font-size: 15px;
    color: var(--teal); letter-spacing: 0.04em; text-transform: uppercase;
  }
  .card-front .contact { position: absolute; left: 30px; top: 152px; font-size: 9.5px; }
  .card-front .address { position: absolute; right: 30px; left: auto; top: 108px; text-align: right; font-size: 9.5px; }
  .card-front .footer-band { height: 22px; }

  .card-back { left: 700px; top: 200px; background: var(--teal); }
  .card-back .wordmark { position: absolute; left: 0; right: 0; top: 72px; text-align: center; color: var(--paper); }
  .card-back .wordmark .name { font-size: 28px; }
  .card-back .wordmark .sub { font-size: 15px; }
  .card-back .swoosh { position: absolute; left: 0; bottom: 0; width: 420px; height: 90px; }
</style>
</head>
<body>
<main class="stationery">

  <section class="letterhead" aria-label="Letterhead">
    <div class="wordmark">
      <span class="name">Harbourline</span>
      <span class="sub">Design Studio</span>
    </div>
    <address class="contact">
      14 Quandong Street<br>
      Ferndale North VIC 3188<br>
      <b>T:</b> 0498 273 461<br>
      <b>E:</b> rosalind@harbourlinedesignstudio.com.au<br>
      <b>W:</b> www.harbourlinedesignstudio.com.au
    </address>
    <div class="footer-band">
      <div class="grey"></div>
      <div class="teal-edge"></div>
      <div class="teal"></div>
    </div>
  </section>

  <section class="card card-back" aria-label="Business card, back">
    <div class="wordmark">
      <span class="name">Harbourline</span>
      <span class="sub">Design Studio</span>
    </div>
    <svg class="swoosh" viewBox="0 0 420 90" aria-hidden="true">
      <path d="M0 90 L0 72 Q220 60 420 10 L420 90 Z" fill="#ffffff"/>
      <path d="M0 90 L0 80 Q220 70 420 26 L420 90 Z" fill="#8c8c8c"/>
    </svg>
  </section>

  <section class="card card-front" aria-label="Business card, front">
    <div class="wordmark">
      <span class="name">Harbourline</span>
      <span class="sub">Design Studio</span>
    </div>
    <address class="contact address">
      14 Quandong Street<br>
      Ferndale North VIC 3188
    </address>
    <h1 class="holder">Rosalind Tebbutt</h1>
    <address class="contact">
      <b>T:</b> 0498 273 461<br>
      <b>E:</b> rosalind@harbourlinedesignstudio.com.au<br>
      <b>W:</b> www.harbourlinedesignstudio.com.au
    </address>
    <div class="footer-band">
      <div class="grey"></div>
      <div class="teal-edge"></div>
      <div class="teal"></div>
    </div>
  </section>

</main>
</body>
</html>
```